Doctors Office Web Design

Name of the business is Lian-Hua Qiu M.D.
We need a web design that is attractive for women that want to see Dr. Lian-Hua Qiu for Obstetrician Gynecology and Pregnancy care. Dr. Qiu earned her degree from Harbor Crest Medical College of obstetrician gynecology. We want to attract women of child bearing ages to come to our offices for health, education, and pregnancies.

Please visit http://www.drqiucare-example.com/ to help you get a feel for who we are. We will be adding some pictures and logo in the next few days.

We are looking for to have pages for and tabs including
About Us- History, Our Staff, Dr. Qiu
Patient Information- Appointments, E-Prescriptions, Payments Accepted, Insurance
Health- General, Sexual, Mental, Affiliates
Pregnancy- Minimally invasive surgery(our specialty), 4-D Ultra Sound, Hospital Affiliations
Media- News,Pictures, Videos
Locations- Palmvale Office, Marlow Office

The colors we would like to use are pastel colors, magenta, and plum

Target Market(s)

Women of all ages with an emphasis on 25-65 year olds

Industry/Entity Type

Business

Requirements
Must have
• Needs to include a location for a our videos and pictures that I will submit shortly. We also want a map to our location or atleast a place for one.
Nice to have
• A place for a google map of our office locations.

```html
<!DOCTYPE html>
<html lang="en">
<head>
<meta charset="utf-8">
<title>Dr. Qiu's – Serving All Areas of Women's Health</title>
<link href="https://fonts.googleapis.com/css2?family=Tinos:ital@0;1&family=Sorts+Mill+Goudy:ital@0;1&family=Open+Sans:wght@400;700&family=Arimo:wght@400;700&display=swap" rel="stylesheet">
<style>
:root{
  --plum:#8a1f80;
  --magenta:#9b2a8f;
  --page:#f4f5f5;
  --panel:#ffffff;
  --footer:#e6e8e8;
  --ink:#333;
  --muted:#8c8c8c;
  --faint:#b8b8b8;
  --rule:#e4e4e4;
  --meta-green:#8ab43a;
  --tab:#2b2b2b;
  --stripe-purple:#8a55a8;
  --stripe-green:#8cc63f;
  --stripe-blue:#8fa9c4;
  --stripe-brown:#9a7a52;
}
*{box-sizing:border-box;margin:0;padding:0}
html,body{width:882px;height:1200px;overflow:hidden}
body{position:relative;background:var(--page);font-family:"Open Sans",sans-serif;color:var(--ink)}
ul{list-style:none}
.abs{position:absolute}

.site-header{left:0;top:0;width:882px;height:116px;background:linear-gradient(#fff,#f6f7f7);text-align:center}
.site-title{position:absolute;left:0;right:0;top:22px;font-family:"Tinos",serif;font-size:35px;color:var(--plum);font-weight:400;letter-spacing:.5px}
.site-tagline{position:absolute;left:0;right:0;top:62px;font-family:"Tinos",serif;font-style:italic;font-size:18px;color:#8d9aa0}

.stripe{left:0;width:882px;height:3px;background:linear-gradient(90deg,
  var(--stripe-blue) 0 14%,var(--stripe-green) 14% 30%,var(--stripe-purple) 30% 45%,var(--stripe-brown) 45% 55%,var(--stripe-green) 55% 72%,var(--stripe-blue) 72% 85%,var(--stripe-purple) 85% 100%)}
.main-nav{left:0;top:119px;width:882px;height:28px;background:#f8f9f9}
.main-nav ul{position:absolute;left:144px;top:0;display:flex;height:28px;align-items:center}
.main-nav li{font-family:"Tinos",serif;font-size:13px;color:var(--plum);margin-right:16px}
.main-nav li.current{background:var(--tab);color:#fff;font-style:italic;font-size:11.5px;padding:0 7px;height:28px;line-height:26px;margin-right:16px;position:relative}
.main-nav li.current::after{content:"";position:absolute;left:50%;bottom:-5px;margin-left:-5px;border:5px solid transparent;border-bottom:0;border-top-color:var(--tab)}

.panel{position:absolute;background:var(--panel);border-top:3px solid var(--stripe-purple);box-shadow:0 1px 3px rgba(0,0,0,.15)}
.widget-title{font-size:6.5px;letter-spacing:.5px;color:var(--faint);text-transform:uppercase;margin:0 0 8px;font-weight:400}
.link-list li{font-size:8px;line-height:11px;color:#555;padding-left:9px;position:relative;margin-bottom:3.3px}
.link-list li::before{content:"·";position:absolute;left:0;color:var(--faint)}
.link-list .who{color:#666}
.link-list .on{color:var(--muted)}

.thumb-list li{display:flex;margin-bottom:6px;font-size:8px;line-height:11px}
.thumb{width:24px;height:24px;flex:none;margin-right:9px;border:1px solid #ddd}
.thumb-list .t-title{display:block;font-size:8px;line-height:11px;color:#444}
.thumb-list .t-date{display:block;font-size:7px;line-height:10px;font-style:italic;color:#c6c6c6}

.slider{left:291px;top:178px;width:290px;height:172px;background:radial-gradient(circle at 72% 70%,#6fb0ff 0,#1b4fc8 22%,#0a1d86 55%,#050c4a 100%);border:2px solid #fff;box-shadow:0 1px 3px rgba(0,0,0,.25)}
.slide-caption{position:absolute;left:40px;right:40px;top:24px;text-align:center;color:#fff}
.slide-caption h2{font-family:"Sorts Mill Goudy",serif;font-weight:400;font-size:20px;line-height:23px}
.slide-caption p{font-family:"Tinos",serif;font-style:italic;font-size:10px;margin-top:6px}
.slide-arrow{position:absolute;top:73px;width:20px;height:22px;background:rgba(255,255,255,.9)}
.slide-arrow svg{display:block;margin:5px auto}

.post-card{position:absolute;width:141px;height:178px;background:var(--panel);box-shadow:0 1px 3px rgba(0,0,0,.18);padding:14px 12px 0}
.post-title{font-family:"Sorts Mill Goudy",serif;font-weight:400;font-size:14px;line-height:16px;text-align:center;color:#333;height:34px}
.post-meta{font-family:"Tinos",serif;font-style:italic;font-size:7.5px;text-align:center;color:var(--faint);margin:4px 0 8px;position:relative}
.post-meta::before,.post-meta::after{content:"";position:absolute;top:5px;width:18px;border-top:1px solid var(--rule)}
.post-meta::before{left:0}.post-meta::after{right:0}
.post-meta b{font-weight:400;color:var(--meta-green)}
.post-body{font-size:7.2px;line-height:10.3px;color:#444}
.post-thumb{float:left;width:45px;height:45px;margin:0 7px 3px 0;border:1px solid #ddd}
.read-more{position:absolute;right:12px;bottom:12px;font-size:5.8px;font-weight:700;color:#333;border:1px solid #eee;padding:3px 5px}

.welcome{left:593px;top:177px;width:141px;height:263px;padding:4px 6px}
.welcome h3{font-family:"Arimo",sans-serif;font-weight:700;font-size:10px;letter-spacing:4.5px;color:var(--plum)}
.welcome p{font-family:"Arimo",sans-serif;font-size:10px;line-height:14.8px;color:var(--magenta);text-align:justify;margin-top:14px;padding-left:2px}
.welcome .email{margin-top:14px;text-align:left}

.pagination{left:415px;top:946px;font-family:"Sorts Mill Goudy",serif;font-size:14px;color:#333;word-spacing:6px}
.pagination .next{position:absolute;left:152px;top:-2px;font-size:17px;font-weight:700}

.site-footer{left:0;top:986px;width:882px;height:214px;background:var(--footer)}
.foot-col{position:absolute;top:30px;width:140px}
.foot-col h4{font-family:"Sorts Mill Goudy",serif;font-weight:400;font-size:15px;color:#333;margin-bottom:10px}
.foot-col .link-list li{font-size:7.5px;line-height:10.5px;color:#556}
.foot-col .text-widget{font-size:7.5px;line-height:10.5px;color:#333;font-weight:700}
</style>
</head>
<body>

<header class="site-header abs">
  <h1 class="site-title">DR. QIU'S</h1>
  <p class="site-tagline">Serving All Areas of Women's Health</p>
</header>

<div class="stripe abs" style="top:116px"></div>
<nav class="main-nav abs">
  <ul>
    <li class="current">Home</li>
    <li>About Us</li>
    <li>Patient Information</li>
    <li>Health</li>
    <li>Pregnancy</li>
    <li>Media</li>
    <li>Locations</li>
  </ul>
</nav>
<div class="stripe abs" style="top:147px"></div>

<aside class="panel" style="left:141px;top:177px;width:141px;height:280px;padding:14px 12px">
  <h3 class="widget-title">Recent Posts</h3>
  <ul class="link-list">
    <li>Nam libero tempore soluta</li>
    <li>Sed neque ipsum pulvinar eu trist</li>
    <li>Cras eu eros id dui porttitor luctus</li>
    <li>Vivamus vitae nibh id quam</li>
    <li>Aenean vulputate fermentum ante</li>
  </ul>
  <h3 class="widget-title" style="margin-top:14px">Recent Comments</h3>
  <ul class="link-list">
    <li><span class="who">Ravi Mehran</span> <span class="on">on</span> Urna eget erat non purus</li>
    <li>Chicken Soup <span class="on">on</span> Nam libero tempore soluta</li>
    <li>Hungry Husband <span class="on">on</span> Nam libero tempore soluta</li>
    <li>tomas <span class="on">on</span> Nam libero tempore soluta</li>
  </ul>
</aside>

<aside class="panel" style="left:141px;top:465px;width:141px;height:412px;padding:18px 14px">
  <h3 class="widget-title">Random Posts</h3>
  <ul class="thumb-list">
    <li><div class="thumb" role="img" aria-label="Post thumbnail: meadow" style="background:linear-gradient(#7fb6e8,#6a9a2e)"></div><div><span class="t-title">Aenean pede elementum</span><span class="t-date">Posted on Sep 28, 2008</span></div></li>
    <li><div class="thumb" role="img" aria-label="Post thumbnail: misty forest" style="background:linear-gradient(#8d8f96,#8a2a2a)"></div><div><span class="t-title">Ut sagittis ultrices urna eget erat non purus</span><span class="t-date">Posted on Sep 5, 2008</span></div></li>
    <li><div class="thumb" role="img" aria-label="Post thumbnail: bamboo" style="background:linear-gradient(90deg,#3d3a24,#b7b48a,#3d3a24)"></div><div><span class="t-title">Cras eu eros id dui porttitor luctus</span><span class="t-date">Posted on Aug 16, 2009</span></div></li>
    <li><div class="thumb" role="img" aria-label="Post thumbnail: tropical bird" style="background:linear-gradient(#4e8a1e,#e0b21e)"></div><div><span class="t-title">Magna suspendisse eleifend at nulla</span><span class="t-date">Posted on Aug 5, 2008</span></div></li>
    <li><div class="thumb" role="img" aria-label="Post thumbnail: dandelion on blue" style="background:radial-gradient(#5a8cff,#0a1d86)"></div><div><span class="t-title">Urna eget erat non purus</span><span class="t-date">Posted on Jul 17, 2008</span></div></li>
  </ul>
  <h3 class="widget-title" style="margin-top:14px">Categories</h3>
  <ul class="link-list">
    <li>Custom Logos</li><li>Design Gallery</li><li>Featured Articles</li><li>Featured Logos</li><li>In The News</li><li>Internet</li><li>News</li><li>Recent Work</li><li>Technology Updates</li><li>Uncategorized</li>
  </ul>
</aside>

<section class="slider abs" role="img" aria-label="Featured slide photo: dandelion seeds on deep blue">
  <div class="slide-caption">
    <h2>Urna eget erat non purus</h2>
    <p>Posted by admin on Jul 17, 2008</p>
  </div>
  <div class="slide-arrow" style="left:3px"><svg width="8" height="12" viewBox="0 0 8 12"><path d="M7 1 2 6l5 5" fill="none" stroke="#999" stroke-width="1.6"/></svg></div>
  <div class="slide-arrow" style="right:3px"><svg width="8" height="12" viewBox="0 0 8 12"><path d="M1 1l5 5-5 5" fill="none" stroke="#999" stroke-width="1.6"/></svg></div>
</section>

<article class="post-card" style="left:291px;top:360px">
  <h2 class="post-title">Nam libero tempore soluta</h2>
  <p class="post-meta">Aug 17, 2009 <b>by</b> admin</p>
  <div class="post-body"><div class="post-thumb" role="img" aria-label="Post photo: portrait" style="background:linear-gradient(#b3c99a,#c79d7a)"></div>Nam libero tempore, cum soluta nobis est eligendi optio cumque nihil impedit quo minus id quod maxime placeat facere possimus, omnis...</div>
  <span class="read-more">READ MORE</span>
</article>
<article class="post-card" style="left:441px;top:360px">
  <h2 class="post-title">Sed neque ipsum pulvinar eu tr...</h2>
  <p class="post-meta">Aug 16, 2009 <b>by</b> admin</p>
  <div class="post-body"><div class="post-thumb" role="img" aria-label="Post photo: tree at sunset" style="background:radial-gradient(#f2b24a,#8a3a10)"></div>Morbi condimentum tempus tincidunt. Sed neque ipsum, pulvinar eu tristique sollicitudin, tincidunt at nisi. Aenean feugiat risus sed...</div>
  <span class="read-more">READ MORE</span>
</article>

<article class="post-card" style="left:291px;top:550px">
  <h2 class="post-title">Cras eu eros id dui porttitor ...</h2>
  <p class="post-meta">Aug 16, 2009 <b>by</b> admin</p>
  <div class="post-body"><div class="post-thumb" role="img" aria-label="Post photo: bamboo stalks" style="background:linear-gradient(90deg,#3d3a24,#c2bf93,#4b4630)"></div>In dolor odio, faucibus at pellentesque ornare, pretium nec diam. Aliquam erat volutpat. Proin vitae sapien et ante convallis...</div>
  <span class="read-more">READ MORE</span>
</article>
<article class="post-card" style="left:441px;top:550px">
  <h2 class="post-title">Vivamus vitae nibh id quam</h2>
  <p class="post-meta">Aug 16, 2009 <b>by</b> admin</p>
  <div class="post-body"><div class="post-thumb" role="img" aria-label="Post photo: bridge at dusk" style="background:linear-gradient(#3a3fb0,#c06ad0,#2a2a6a)"></div>Pellentesque et ante at dui condimentum venenatis nec eu quam. Ut consequat orci ut mi luctus eget luctus est viverra. Praesent...</div>
  <span class="read-more">READ MORE</span>
</article>

<article class="post-card" style="left:291px;top:740px">
  <h2 class="post-title">Aenean vulputate fermentum ant...</h2>
  <p class="post-meta">Aug 16, 2009 <b>by</b> admin</p>
  <div class="post-body"><div class="post-thumb" role="img" aria-label="Partner badge" style="background:#fff;border-color:#fff"><div style="width:26px;height:30px;margin:4px auto;background:#7a3a9a;border-radius:50%"></div></div>Phasellus mauris elit, porta a placerat eget, lobortis vel ipsum. Maecenas at ligula consequat. Vivamus massa lorem,...</div>
  <span class="read-more">READ MORE</span>
</article>
<article class="post-card" style="left:441px;top:740px">
  <h2 class="post-title">Ut sagittis ultrices urna eget...</h2>
  <p class="post-meta">Sep 5, 2008 <b>by</b> admin</p>
  <div class="post-body"><div class="post-thumb" role="img" aria-label="Post photo: misty red forest" style="background:linear-gradient(#9a9ba2,#8a2a2a)"></div>Sed tempor lectus in risus. Nullam vestibulum, dolor eu pulvinar condimentum, urna neque aliquet ipsum, in blandit velit nunc eget...</div>
  <span class="read-more">READ MORE</span>
</article>

<aside class="panel welcome">
  <h3>Welcome to...</h3>
  <p>Dr. Lian-Hua Qiu's website. Here you will be able to find information about both of our offices, meet Dr. Qiu and her staff, and browse through our women's health links to learn more about pregnancy, nutrition, exercise, and other women's health issues. Have fun and if you have any questions, feel free to contact us at</p>
  <p class="email">drqiu@qiucare.net</p>
</aside>

<aside class="panel" style="left:593px;top:452px;width:141px;height:453px;padding:16px 12px">
  <h3 class="widget-title">Popular Posts</h3>
  <ul class="thumb-list">
    <li><div class="thumb" role="img" aria-label="Post thumbnail: misty forest" style="background:linear-gradient(#8d8f96,#8a2a2a)"></div><div><span class="t-title">Ut sagittis ultrices urna eget erat non purus</span><span class="t-date">Posted on Sep 5, 2008</span></div></li>
    <li><div class="thumb" role="img" aria-label="Post thumbnail: dandelion on blue" style="background:radial-gradient(#5a8cff,#0a1d86)"></div><div><span class="t-title">Urna eget erat non purus</span><span class="t-date">Posted on Jul 17, 2008</span></div></li>
    <li><div class="thumb" role="img" aria-label="Post thumbnail: portrait" style="background:linear-gradient(#b3c99a,#c79d7a)"></div><div><span class="t-title">Nam libero tempore soluta</span><span class="t-date">Posted on Aug 17, 2009</span></div></li>
    <li><div class="thumb" role="img" aria-label="Post thumbnail: warm light" style="background:radial-gradient(#f3d08a,#3a2410)"></div><div><span class="t-title">Neque porro quisquam est qui</span><span class="t-date">Posted on Sep 4, 2008</span></div></li>
    <li><div class="thumb" role="img" aria-label="Post thumbnail: tree at sunset" style="background:radial-gradient(#f2b24a,#8a3a10)"></div><div><span class="t-title">Sed neque ipsum pulvinar eu trist</span><span class="t-date">Posted on Aug 16, 2009</span></div></li>
  </ul>
  <h3 class="widget-title" style="margin-top:16px">Blogroll</h3>
  <ul class="link-list">
    <li>Documentation</li><li>Plugins</li><li>Suggest Ideas</li><li>Support Forum</li><li>Themes</li><li>PressLeaf Blog</li><li>PressLeaf Planet</li>
  </ul>
  <h3 class="widget-title" style="margin-top:14px">Meta</h3>
  <ul class="link-list">
    <li>Log in</li><li>Entries RSS</li><li>Comments RSS</li><li>PressLeaf.org</li>
  </ul>
</aside>

<nav class="pagination abs">1 2 3 <span class="next">»</span></nav>

<div class="stripe abs" style="top:984px"></div>
<footer class="site-footer abs">
  <section class="foot-col" style="left:141px">
    <h4>Recent Posts</h4>
    <ul class="link-list">
      <li>Nam libero tempore soluta</li><li>Sed neque ipsum pulvinar eu trist</li><li>Cras eu eros id dui porttitor luctus</li><li>Vivamus vitae nibh id quam</li><li>Aenean vulputate fermentum ante</li><li>Ut sagittis ultrices urna eget erat non purus</li><li>Neque porro quisquam est qui</li>
    </ul>
  </section>
  <section class="foot-col" style="left:292px">
    <h4>Text Widget</h4>
    <p class="text-widget">Etiam pharetra scelerisque diam. Maecenas varius augue vel urna. Vestibulum erat nisl, fringilla vel, mollis et, aliquam non, elit. Nulla malesuada turpis nec velit. Donec vitae sem a metus dictum molestie. Ut dignissim, odio non porttitor convallis, sapien leo viverra lorem, a consequat mauris erat sit amet dui.</p>
  </section>
  <section class="foot-col" style="left:444px">
    <h4>Archives</h4>
    <ul class="link-list">
      <li>August 2009</li><li>September 2008</li><li>August 2008</li><li>July 2008</li><li>January 2008</li><li>July 2007</li><li>September 2006</li>
    </ul>
  </section>
  <section class="foot-col" style="left:596px;width:160px">
    <h4>Recent Comments</h4>
    <ul class="link-list">
      <li>Ravi Mehran on Urna eget erat non purus</li><li>Chicken Soup on Nam libero tempore soluta</li><li>Hungry Husband on Nam libero tempore soluta</li><li>tomas on Nam libero tempore soluta</li><li>Ardenart on Vivamus vitae nibh id quam</li>
    </ul>
  </section>
</footer>

</body>
</html>
```